We specialize in pizza, pasta and salads and are now offering TAKE & BAKE and GRAB & GO ...

Looking for either a 8.5" x 11" or similar for a instore display. WILL BE ON A SWIVELING HOLDER to catch customers attention.

**THIS IS A DOUBLE SIDED PRINT**

ONE SIDE will consist of WHAT'S FOR DINNER TONIGHT? and the following:
* Take & Bake"
* "Baked Pasta"
* Freshly made in house
* Lasagna
$13.50
- please include attached closeup picture and logo

THE OTHER SIDE will consist of
mini charcutier board.
* snack size charcutier delight *
* Enjoy the flavors of gourmet snacking, all in one convenient box!

PRICE $8.99

Winning design will be commissioned to design labels for "grab and go" for take and bake pasta, charcuterie box, pasta salads, candy etc.

Thank you and please do not hesitate to ask any questions.

www.castelmopizza.ca
www.pebbletop.ca
Logo to be interchanged as they are affiliated meaning PebbleTop is a brand within Castelmo pizza.

Low design quality

our target market is customers who have already entered our business. This is to upsel

We are in a self serve enviroment and target business people

• must be clean and catchy. We are located in a professional business community.
• Must be appealing, appetizing and utilize our website colors
• should not have any carton drawings and not be cluttered (busy)

```html
<!DOCTYPE html>
<html lang="en">
<head>
<meta charset="utf-8">
<title>Castelmo Pizza – Take &amp; Bake and Grab &amp; Go Display</title>
<link rel="stylesheet" href="https://fonts.googleapis.com/css2?family=Permanent+Marker&family=Oswald:wght@400;500&display=block">
<style>
  :root {
    --stage: #b3b3b3;
    --stage-light: #c2c2c2;
    --paper-warm: #f2f2f2;
    --paper-cool: #eff6fa;
    --ink: #454545;
    --brand-red: #cc3333;
    --white: #ffffff;
    --band-grey: #4a4a4a;
  }
  html, body {
    margin: 0;
    padding: 0;
    width: 1200px;
    height: 933px;
    overflow: hidden;
    background: var(--stage);
  }
  .stage {
    position: relative;
    width: 1200px;
    height: 933px;
    background: var(--stage);
  }
  .stage-tint {
    position: absolute;
    left: 0;
    top: 0;
    width: 561px;
    height: 790px;
    background: var(--stage-light);
  }
  .display-side {
    position: absolute;
    width: 560px;
    height: 793px;
    display: block;
  }
  .side-dinner { left: 31px; top: 44px; }
  .side-charcuterie { left: 607px; top: 99px; }

  .paper-warm { fill: var(--paper-warm); }
  .paper-cool { fill: var(--paper-cool); }
  .brand-name {
    font-family: "Oswald", sans-serif;
    font-weight: 400;
    font-size: 15px;
    letter-spacing: 1px;
    fill: var(--ink);
  }
  .headline {
    font-family: "Permanent Marker", "Oswald", sans-serif;
    font-size: 100px;
    fill: var(--ink);
  }
  .headline-sub { font-size: 80px; }
  .accent { fill: var(--brand-red); }
  .details {
    font-family: "Oswald", sans-serif;
    font-weight: 500;
    font-size: 29px;
    fill: var(--ink);
  }
  .details-small { font-size: 24px; }
  .wave-red { fill: var(--brand-red); }
  .wave-white { fill: var(--white); }
  .wave-grey { fill: var(--band-grey); }
  .price-tag { fill: var(--brand-red); }
  .price {
    font-family: "Permanent Marker", "Oswald", sans-serif;
    font-size: 54px;
    fill: var(--white);
  }
</style>
</head>
<body>
<main class="stage">
  <div class="stage-tint"></div>

  <!-- Side one: dinner -->
  <svg class="display-side side-dinner" viewBox="0 0 560 793" xmlns="http://www.w3.org/2000/svg">
    <defs>
      <linearGradient id="lasagna-tones" x1="0" y1="0" x2="0.4" y2="1">
        <stop offset="0" stop-color="#e0a93a"/>
        <stop offset="0.35" stop-color="#6b4a2a"/>
        <stop offset="0.6" stop-color="#e8dcc4"/>
        <stop offset="1" stop-color="#c98a3c"/>
      </linearGradient>
    </defs>
    <rect class="paper-warm" width="560" height="793"/>
    <text class="brand-name" x="281" y="29" text-anchor="middle">CASTELMOPIZZA</text>

    <text class="headline" x="32" y="152" textLength="480" lengthAdjust="spacingAndGlyphs">WHAT'S FOR</text>
    <text class="headline accent" x="26" y="270" textLength="314" lengthAdjust="spacingAndGlyphs">DINNER</text>
    <text class="headline" x="29" y="388" textLength="318" lengthAdjust="spacingAndGlyphs">TONIGHT</text>

    <text class="details" x="33" y="512" textLength="135" lengthAdjust="spacingAndGlyphs">TAKE <tspan class="accent">&amp;</tspan> BAKE</text>
    <text class="details" x="33" y="556" textLength="141" lengthAdjust="spacingAndGlyphs">BAKED PASTA</text>
    <text class="details" x="33" y="600" textLength="157" lengthAdjust="spacingAndGlyphs">FRESHLY MADE</text>
    <text class="details" x="33" y="644" textLength="199" lengthAdjust="spacingAndGlyphs">IN HOUSE LASAGNA</text>

    <path class="wave-red" d="M560,278 C470,322 340,392 325,500 C312,600 330,700 212,793 L560,793 Z"/>
    <path class="wave-white" d="M560,284 C474,328 346,397 331,502 C318,602 336,702 219,793 L560,793 Z"/>
    <path class="wave-grey" d="M560,292 C480,336 350,404 336,505 C324,605 342,704 227,793 L560,793 Z"/>
    <path fill="url(#lasagna-tones)" role="img" aria-label="Close-up photo of baked lasagna with stretching melted cheese"
          d="M560,292 C482,337 358,407 345,508 C334,607 350,706 237,793 L560,793 Z"/>

    <path class="price-tag" d="M0,718 C70,692 180,682 212,728 C228,752 210,778 198,793 L0,793 Z"/>
    <text class="price" x="24" y="763" textLength="154" lengthAdjust="spacingAndGlyphs">$13.50</text>
  </svg>

  <!-- Side two: charcuterie -->
  <svg class="display-side side-charcuterie" viewBox="0 0 560 793" xmlns="http://www.w3.org/2000/svg">
    <defs>
      <linearGradient id="charcuterie-tones" x1="0.8" y1="0" x2="0.2" y2="1">
        <stop offset="0" stop-color="#d9b276"/>
        <stop offset="0.25" stop-color="#a9c47a"/>
        <stop offset="0.5" stop-color="#4a2630"/>
        <stop offset="0.8" stop-color="#c7606a"/>
        <stop offset="1" stop-color="#6a4a38"/>
      </linearGradient>
    </defs>
    <rect class="paper-cool" width="560" height="793"/>
    <text class="brand-name" x="284" y="29" text-anchor="middle">CASTELMOPIZZA</text>

    <text class="headline headline-sub" x="28" y="192" textLength="123" lengthAdjust="spacingAndGlyphs">MINI</text>
    <text class="headline headline-sub accent" x="172" y="192" textLength="360" lengthAdjust="spacingAndGlyphs">CHARCUTIER</text>
    <text class="headline headline-sub" x="31" y="279" textLength="198" lengthAdjust="spacingAndGlyphs">BOARD</text>

    <text class="details details-small" x="24" y="382" textLength="294" lengthAdjust="spacingAndGlyphs">SNACK SIZE CHARCUTIER DELIGHT</text>
    <text class="details details-small" x="24" y="419" textLength="291" lengthAdjust="spacingAndGlyphs">ENJOY THE FLAVORS OF <tspan class="accent">GOURMET</tspan></text>
    <text class="details details-small" x="24" y="456" textLength="195" lengthAdjust="spacingAndGlyphs"><tspan class="accent">SNACKING</tspan>, ALL IN ONE</text>
    <text class="details details-small" x="24" y="493" textLength="157" lengthAdjust="spacingAndGlyphs">CONVENIENT BOX!</text>

    <path class="wave-red" d="M560,279 C470,324 340,394 326,500 C314,600 332,700 214,793 L560,793 Z"/>
    <path class="wave-white" d="M560,285 C474,330 346,399 332,502 C320,602 338,702 221,793 L560,793 Z"/>
    <path class="wave-grey" d="M560,293 C480,338 350,406 337,505 C326,605 344,704 229,793 L560,793 Z"/>
    <path fill="url(#charcuterie-tones)" role="img" aria-label="Photo of a charcuterie board with cured meats, cheese, grapes, figs, crackers and jam"
          d="M560,293 C482,339 358,409 346,508 C336,607 352,706 239,793 L560,793 Z"/>

    <path class="price-tag" d="M0,718 C70,692 185,682 216,728 C232,752 214,778 202,793 L0,793 Z"/>
    <text class="price" x="40" y="760" textLength="132" lengthAdjust="spacingAndGlyphs">$8.99</text>
  </svg>
</main>
</body>
</html>
```